Postcard to Sell Ads to business

I am in need of a very professional, clean but SEXY postcard that creates excitement to the business owner and gets them to call me to learn more. I expect source file (psd) with final files.

Postcard Requirements

FULL COLOR - FRONT And Back
All Text Editable including heading font uses
Use of Vibrant colors and vector ICONS
Backside should contain text and images as well

Items to Include in design

Benefits of Advertising
- 365 Days of Advertising
- Under $.04 per home
- Unlimited Social Media Attention
- Increased Revenue
- 100% Managed for you

Did You Know Facts
87% of online users depend on the internet to access local discounts
Business who use the internet to promote and sell thier offline goods and services have grown 46% faster over the past two years.

This postcard will sell my Direct Mailer I offer to go along with my local business directoy - http://www.elmstreetsavers.example

Visually connecting this service to a local nature is imperitive.

Target Market(s)

Local area business, Retail, Restaurant, Media, and anything sold to consumers.

Industry/Entity Type

Advertising

Font styles to use
Sans Serif

Requirements
Must have
• Return Address as:
• Elm Lane Savers
• P.O Box 758
• Brookfield, CT 06804
• 1-860-555-0172
• COLOR
• Text based "Logo": Elm Lane Savers
• Include a emphasis on just $.04/home
• Icons/infographic use
Nice to have
• Vector based character image
• Your Ad Here Image as a representation to what this postcard is about
Should not have
• Large amount of whitespace

```html
<!DOCTYPE html>
<html lang="en">
<head>
<meta charset="utf-8">
<title>Elm Lane Savers – Advertising Postcard</title>
<link href="https://fonts.googleapis.com/css2?family=Roboto:wght@300;400;500;700;900&family=Roboto+Condensed:wght@700&display=swap" rel="stylesheet">
<style>
  :root {
    --backdrop: #bfcac9;
    --navy: #1f3a5f;
    --ink: #0c0c0c;
    --yellow: #f2d422;
    --card-light: #ffffff;
    --card-tint: #e3e3f2;
    --panel-dark: #3b5876;
    --panel-light: #8ea2b6;
    --white: #ffffff;
  }
  * { margin: 0; padding: 0; box-sizing: border-box; }
  html, body { width: 1200px; height: 1200px; overflow: hidden; }
  body {
    background: var(--backdrop);
    font-family: "Roboto", Arial, sans-serif;
    color: var(--ink);
    position: relative;
  }
  .postcard {
    position: absolute;
    overflow: hidden;
    background: linear-gradient(100deg, var(--card-light) 0%, var(--card-tint) 100%);
    box-shadow: 8px 10px 14px rgba(60, 75, 90, 0.35);
  }
  .postcard--front { left: 272px; top: 42px; width: 696px; height: 540px; }
  .postcard--back  { left: 274px; top: 618px; width: 693px; height: 539px; }
  .shapes { position: absolute; inset: 0; width: 100%; height: 100%; }

  /* Company name */
  .brand {
    position: absolute;
    display: flex; align-items: center; gap: 9px;
  }
  .brand__dot { border-radius: 50%; background: var(--yellow); flex: none; }
  .brand__name { font-weight: 700; line-height: 1; white-space: nowrap; }
  .brand--front { left: 22px; top: 36px; color: var(--navy); }
  .brand--front .brand__dot { width: 20px; height: 20px; }
  .brand--front .brand__name { font-size: 22px; }
  .brand--back { left: 188px; top: 80px; color: var(--white); gap: 7px; }
  .brand--back .brand__dot { width: 13px; height: 13px; }
  .brand--back .brand__name { font-size: 14px; }

  /* Front copy */
  .headline { position: absolute; left: 26px; top: 205px; line-height: 1; }
  .headline__main { display: block; font-size: 57px; font-weight: 700; letter-spacing: -0.5px; }
  .headline__sub { display: block; font-size: 36px; font-weight: 700; margin-top: 4px; }

  .fact { position: absolute; }
  .fact--users { left: 26px; top: 390px; font-size: 19px; line-height: 1.25; }
  .fact__figure { font-size: 52px; font-weight: 300; line-height: 1; letter-spacing: -1px; }
  .fact__strong { font-weight: 500; }
  .fact--growth {
    left: 286px; top: 412px; width: 394px;
    font-family: "Roboto Condensed", "Arial Narrow", sans-serif;
    font-weight: 700; font-size: 18px; line-height: 21px;
  }
  .fact__line { display: block; text-align: justify; text-align-last: justify; white-space: nowrap; }
  .fact__line--last { text-align: right; text-align-last: right; }

  .contact-strip {
    position: absolute; left: 0; right: 0; bottom: 0; height: 31px;
    background: var(--yellow);
    display: flex; align-items: center; justify-content: space-between;
    padding: 0 16px 0 18px;
    font-size: 14px; font-weight: 700;
  }
  .contact { display: flex; align-items: center; gap: 9px; white-space: nowrap; }
  .icon { width: 16px; height: 16px; flex: none; }

  /* Back */
  .back-topbar { position: absolute; left: 0; top: 0; width: 100%; height: 18px; background: var(--yellow); }
  .benefits {
    position: absolute; left: 0; top: 294px; width: 334px; height: 184px;
    background: linear-gradient(90deg, var(--panel-dark) 0%, var(--panel-light) 100%);
    color: var(--white);
    padding: 20px 0 0 19px;
  }
  .benefits__title { color: var(--yellow); font-size: 29px; font-weight: 500; line-height: 1; margin-bottom: 8px; white-space: nowrap; }
  .benefits__list { list-style: none; }
  .benefits__item { display: flex; align-items: center; font-size: 17.5px; font-weight: 500; line-height: 20.8px; }
  .benefits__item::before {
    content: ""; width: 8px; height: 8px; border-radius: 50%;
    background: var(--yellow); margin: 0 20px 0 2px; flex: none;
  }
  .stamp-box {
    position: absolute; left: 550px; top: 34px; width: 92px; height: 92px;
    background: var(--white); border: 1.5px solid var(--yellow);
  }
  .address-line { position: absolute; left: 355px; width: 297px; height: 1px; background: #7a7a86; }
  .return-bar {
    position: absolute; left: 0; bottom: 0; width: 100%; height: 37px;
    background: var(--navy); color: var(--white);
    font-size: 13.5px; font-weight: 500;
  }
  .return-bar .contact { position: absolute; top: 0; height: 37px; gap: 10px; }
  .return-bar .contact--address { left: 36px; }
  .return-bar .contact--phone { left: 299px; }
  .return-bar .contact--web { left: 468px; }
</style>
</head>
<body>

<!-- FRONT -->
<section class="postcard postcard--front">
  <svg class="shapes" viewBox="0 0 696 540" preserveAspectRatio="none">
    <defs>
      <radialGradient id="techGlow" cx="70%" cy="40%" r="60%">
        <stop offset="0" stop-color="#b9d8ee"/>
        <stop offset="0.35" stop-color="#4d7aa3"/>
        <stop offset="1" stop-color="#16243a"/>
      </radialGradient>
    </defs>
    <path role="img" aria-label="Photo: open hands holding a laptop, tablet, phone and a glowing globe linked by a network of people icons"
          d="M304,0 L696,0 L696,150 C640,205 600,232 556,238 C460,250 380,215 200,160 C230,100 260,50 304,0 Z" fill="url(#techGlow)"/>
    <path d="M0,186 C80,160 170,160 250,185 C360,220 450,250 556,238 C480,300 380,355 240,368 C140,376 60,340 0,306 Z" fill="var(--yellow)"/>
    <path d="M300,362 C450,340 600,300 696,245 L696,150 C650,200 600,230 556,238 C480,300 400,345 300,362 Z" fill="var(--ink)"/>
    <path d="M240,368 C420,350 580,320 696,265 L696,292 C580,338 420,362 240,368 Z" fill="var(--navy)"/>
    <path d="M0,498 C250,500 500,500 696,490 L696,512 L0,512 Z" fill="var(--ink)"/>
  </svg>

  <div class="brand brand--front">
    <span class="brand__dot"></span>
    <span class="brand__name">Elm Lane Savers</span>
  </div>

  <h1 class="headline">
    <span class="headline__main">a emphasis</span>
    <span class="headline__sub">on just $.04/home</span>
  </h1>

  <p class="fact fact--users">
    <span class="fact__figure">87%</span>of online users<br>
    depend on the internet to<br>
    <span class="fact__strong">access local discounts</span>
  </p>

  <p class="fact fact--growth">
    <span class="fact__line">Business who use the internet to promote and sell</span>
    <span class="fact__line">thier offline goods and services have grown 46%</span>
    <span class="fact__line fact__line--last">faster over the past two years.</span>
  </p>

  <footer class="contact-strip">
    <span class="contact">
      <svg class="icon" viewBox="0 0 16 16"><rect x="4" y="1" width="8" height="14" rx="1.5" fill="none" stroke="currentColor" stroke-width="1.6"/><circle cx="8" cy="12.5" r="0.9" fill="currentColor"/></svg>
      1-860-555-0172
    </span>
    <span class="contact">
      <svg class="icon" viewBox="0 0 16 16" fill="none" stroke="currentColor" stroke-width="1.2"><circle cx="8" cy="8" r="6.5"/><ellipse cx="8" cy="8" rx="3" ry="6.5"/><path d="M1.5 8h13M2.5 4.8h11M2.5 11.2h11"/></svg>
      www.elmstreetsavers.example
    </span>
  </footer>
</section>

<!-- BACK -->
<section class="postcard postcard--back">
  <div class="back-topbar"></div>
  <svg class="shapes" viewBox="0 0 693 539" preserveAspectRatio="none">
    <defs>
      <linearGradient id="handshakeTone" x1="0" y1="0" x2="1" y2="1">
        <stop offset="0" stop-color="#3a5578"/>
        <stop offset="0.45" stop-color="#d9b7a0"/>
        <stop offset="0.75" stop-color="#a9c1dc"/>
        <stop offset="1" stop-color="#e9eef5"/>
      </linearGradient>
    </defs>
    <path d="M140,58 C200,40 280,25 334,18 L334,174 C290,150 220,100 140,58 Z" fill="var(--ink)"/>
    <path d="M0,86 C40,50 100,50 140,66 C220,110 290,190 334,212 L320,246 C220,260 100,300 0,270 Z" fill="var(--yellow)"/>
    <path role="img" aria-label="Photo: two business people shaking hands in front of office towers"
          d="M0,112 C40,82 95,78 135,92 C210,130 270,190 330,214 C250,240 150,285 0,262 Z" fill="url(#handshakeTone)"/>
    <path d="M0,258 C80,296 200,272 334,228 L334,300 L0,300 Z" fill="var(--navy)"/>
  </svg>

  <div class="brand brand--back">
    <span class="brand__dot"></span>
    <span class="brand__name">Elm Lane Savers</span>
  </div>

  <div class="benefits">
    <h2 class="benefits__title">Benefits of Advertising</h2>
    <ul class="benefits__list">
      <li class="benefits__item">365 Days of Advertising</li>
      <li class="benefits__item">Under $.04 per home</li>
      <li class="benefits__item">Unlimited Social Media Attention</li>
      <li class="benefits__item">Increased Revenue</li>
      <li class="benefits__item">100% Managed for you</li>
    </ul>
  </div>

  <div class="stamp-box"></div>
  <div class="address-line" style="top:302px"></div>
  <div class="address-line" style="top:331px"></div>
  <div class="address-line" style="top:359px"></div>

  <footer class="return-bar">
    <span class="contact contact--address">
      <svg class="icon" viewBox="0 0 16 16" fill="currentColor"><path d="M8 1.5 1 8h2v6.5h4v-4h2v4h4V8h2z"/></svg>
      P.O Box 758 Brookfield, CT 06804
    </span>
    <span class="contact contact--phone">
      <svg class="icon" viewBox="0 0 16 16"><rect x="4" y="1" width="8" height="14" rx="1.5" fill="none" stroke="currentColor" stroke-width="1.6"/><circle cx="8" cy="12.5" r="0.9" fill="currentColor"/></svg>
      1-860-555-0172
    </span>
    <span class="contact contact--web">
      <svg class="icon" viewBox="0 0 16 16" fill="none" stroke="currentColor" stroke-width="1.2"><circle cx="8" cy="8" r="6.5"/><ellipse cx="8" cy="8" rx="3" ry="6.5"/><path d="M1.5 8h13M2.5 4.8h11M2.5 11.2h11"/></svg>
      www.elmstreetsavers.example
    </span>
  </footer>
</section>

</body>
</html>
```